Flyer Design

I'm looking for a new flyer design to help promote our landscape company, and some of our main service for the up and coming season. We're trying to position ourselves as a leader in our market, so obviously quality is important to us.

Our current promotion is 25% off the first month with signup of annual service.

Phone Number: (816) 555-0193
Website: gardelvista.com
Our tagline: "Your hands are full... Let us help"

The call to action: direct them to our website for a detailed list of services and to receive a free quote.

You're welcome to add your own wording and punctuation. If I like the design I will provide feedback accordingly.

I have attached a jpg of our logo to help with design colors. I will provide the vector file upon completion of this project.

Also, I've attached a few photos that I had on hand of our companies work that may help with the design. Obviously I don't want to use them all, but there are a couple just to help out. I'm not opposed to stock photos either.
Thanks

Target Market(s)

We market to high end customers, generally with home between $500k-$2mil, or household income over $200k. Quality and creativity are most important to us.

Industry/Entity Type

Landscape

Requirements
Must have
• Creativity, easy to read, modern style.

```html
<!DOCTYPE html>
<html lang="en">
<head>
<meta charset="utf-8">
<title>Gardel Vista – Lawn &amp; Landscape Flyer</title>
<link rel="stylesheet" href="https://fonts.googleapis.com/css2?family=Ultra&display=swap">
<style>
  :root {
    --grass-light: #7fcf3a;
    --grass-mid: #5fb52a;
    --grass-dark: #3f8f1c;
    --panel: rgba(220, 240, 190, 0.55);
    --ink: #1c1c14;
    --accent: #f04e23;
  }
  * { margin: 0; padding: 0; box-sizing: border-box; }
  html, body { width: 1200px; height: 1000px; overflow: hidden; }
  body { font-family: "Ultra", "Rockwell Extra Bold", serif; color: var(--ink); }

  .flyer { position: relative; width: 1200px; height: 1000px; overflow: hidden; }

  .lawn-backdrop {
    position: absolute; inset: 0;
    background:
      repeating-linear-gradient(160deg, rgba(255,255,255,0.07) 0 90px, rgba(0,0,0,0.06) 90px 180px),
      radial-gradient(ellipse at 50% 40%, var(--grass-light), var(--grass-mid) 60%, var(--grass-dark));
  }

  .brand {
    position: absolute; left: 0; right: 0; top: 48px;
    display: flex; align-items: center; justify-content: center; gap: 22px;
  }
  .brand-dot { width: 54px; height: 54px; border-radius: 50%; background: var(--accent); }
  .brand-name { font-size: 68px; letter-spacing: 2px; color: var(--ink); line-height: 1; }

  .headline { position: absolute; left: 0; right: 0; text-align: center; white-space: nowrap; }
  .tagline { top: 160px; font-size: 30px; letter-spacing: 1px; }
  .promo {
    top: 222px; left: 50%; right: auto; transform: translateX(-50%);
    font-size: 24px; letter-spacing: 1px; color: #fff;
    background: var(--accent); padding: 10px 28px; border-radius: 40px;
  }

  .services {
    position: absolute; left: 80px; top: 312px; width: 1045px; height: 416px;
    background: var(--panel);
  }
  .service-badge {
    position: absolute; width: 112px; height: 76px; border-radius: 50%;
    background: var(--accent);
  }
  .service-text {
    position: absolute; font-size: 18px; line-height: 24px;
    letter-spacing: 1px; white-space: nowrap;
  }

  .contact { position: absolute; left: 0; right: 0; text-align: center; white-space: nowrap; }
  .phone { top: 734px; font-size: 48px; letter-spacing: 3px; line-height: 1; }
  .cta { font-size: 30px; letter-spacing: 2px; line-height: 1; }
  .cta-1 { top: 795px; }
  .cta-2 { top: 843px; }
  .cta-3 { top: 893px; font-size: 27px; }
  .web { top: 932px; font-size: 52px; letter-spacing: 3px; line-height: 1; }
</style>
</head>
<body>
<main class="flyer">
  <div class="lawn-backdrop" role="img" aria-label="Freshly mowed striped green lawn"></div>

  <header class="brand">
    <span class="brand-dot"></span>
    <span class="brand-name">GARDEL VISTA</span>
  </header>

  <p class="headline tagline">Your hands are full... Let us help</p>
  <p class="headline promo">25% off your first month with annual service signup</p>

  <section class="services">
    <span class="service-badge" style="left:15px; top:4px;"></span>
    <p class="service-text" style="left:168px; top:24px;">We use only top quality stand-on aerators that<br>&nbsp;provide hydraulic downward pressure<br>&nbsp;to maximize core depth with every<br>&nbsp;individual plug</p>

    <span class="service-badge" style="left:15px; top:126px;"></span>
    <p class="service-text" style="left:177px; top:134px;">We trim all types of shrubs and hedges,<br>perennials, decorative grass<br>and ornamental trees and bushes<br>with protection from insects</p>

    <span class="service-badge" style="left:15px; top:228px;"></span>
    <p class="service-text" style="left:177px; top:244px;">Residential driveways, sidewalks,<br>commercial parking lots as well as ice management.</p>

    <span class="service-badge" style="left:17px; top:326px;"></span>
    <p class="service-text" style="left:177px; top:322px;">Lawn care service includes mowing the entire yard,<br>line trimming around all trees, flowerbeds,<br>yard decorations and edging all sidewalks,<br>patios, and driveways.</p>
  </section>

  <p class="contact phone">tel: 816.555.0193</p>
  <p class="contact cta cta-1">To see a full list of our services and to</p>
  <p class="contact cta cta-2">receive a free quote</p>
  <p class="contact cta cta-3">please go to</p>
  <p class="contact web">www.gardelvista.com</p>
</main>
</body>
</html>
```